International Bike and Bike Clothing distribution business needs business card design. Business is

We need a business card design for our Bike Brand distribution business. Want the company name on one side and rep/gm contact details on other side. Contact details would include, name, title, email, phone, postal address. Needs to be a bit edgy, dealing with a sporting/cycling community so can be casual but professional. Company name is 'Brisko Bike Brands' and would like to see 'Brisko' in a cursive font (similar to Velmo cycling brand) and 'Bike Brands' to be separate or below 'Brisko' in a simple capital letter font. The inclusion of an image reflective of the nature of the business would be encouraged.

Industry/Entity Type

Business

Contact Information for Business Card

2 cards with following information;

Dorian Pelt
Managing Director
E dorian@briskobikebrands-example.ae
M +971 (0) 56 482 3107
Trade Lic. No. TBA

Minna Pelt
Account Manager
E minna@briskobikebrands-example.ae
P +971 (0) 56 916 2583
Trade Lic. No. TBA

Requirements
Must have
• Full company name is 'Brisko Bike Brands'
• Would like Brisko to be separate and in a font similar to Velmo Cycling clothing, and would like Bike Brands to be in capitals below. Would consider if an image of a push bike between the text was presented.

```html
<!DOCTYPE html>
<html lang="en">
<head>
<meta charset="utf-8">
<title>Brisko Bike Brands – Business Cards</title>
<link rel="stylesheet" href="https://fonts.googleapis.com/css2?family=Josefin+Sans:wght@300;400&family=Cormorant+SC:wght@500&display=swap">
<style>
  :root {
    --bg-warm: #fbf3ee;
    --bg-cool: #ededed;
    --card: #222223;
    --card-edge: #2c2c2d;
    --ink: #f4f4f4;
    --ink-soft: #cfcfcf;
    --teal: #2fa99a;
    --teal-deep: #1d6f68;
    --rose: #dc5a6c;
    --rose-deep: #8a3a44;
  }
  * { box-sizing: border-box; margin: 0; padding: 0; }
  html, body { width: 1200px; height: 365px; overflow: hidden; }
  body {
    position: relative;
    background: linear-gradient(90deg, var(--bg-warm), var(--bg-cool));
    font-family: "Josefin Sans", sans-serif;
    color: var(--ink);
  }
  .swatch { position: absolute; left: 258px; width: 34px; height: 34px; border-radius: 50%; }
  .swatch--teal { top: 72px; background: var(--teal); }
  .swatch--rose { top: 259px; background: var(--rose); }

  .card {
    position: absolute; width: 300px; height: 162px; border-radius: 14px;
    background: radial-gradient(circle at 50% 45%, var(--card-edge), var(--card));
    overflow: hidden; box-shadow: 0 3px 8px rgba(0,0,0,.25);
  }
  .card--front-teal { left: 310px; top: 8px; }
  .card--back-teal  { left: 625px; top: 8px; }
  .card--front-rose { left: 310px; top: 195px; }
  .card--back-rose  { left: 625px; top: 195px; }

  .facets { position: absolute; top: 0; bottom: 0; width: 62px; }
  .facets--right { right: 0; }
  .facets--left { left: 0; }
  .facets--teal.facets--right { background: linear-gradient(90deg, rgba(29,111,104,.1), var(--teal-deep) 45%, var(--teal)); }
  .facets--teal.facets--left  { background: linear-gradient(270deg, rgba(29,111,104,.1), var(--teal-deep) 45%, var(--teal)); }
  .facets--rose.facets--right { background: linear-gradient(90deg, rgba(138,58,68,.1), var(--rose-deep) 45%, var(--rose)); }
  .facets--rose.facets--left  { background: linear-gradient(270deg, rgba(138,58,68,.1), var(--rose-deep) 45%, var(--rose)); }

  .wordmark {
    position: absolute; left: 0; right: 0; top: 50px; text-align: center;
    font-weight: 300; color: var(--ink); text-transform: uppercase;
  }
  .wordmark__name { display: block; font-size: 26px; letter-spacing: 3px; line-height: 28px; }
  .wordmark__line { display: block; font-size: 11px; letter-spacing: 4px; line-height: 16px; }

  .site {
    position: absolute; bottom: 12px; left: 0; right: 0;
    display: flex; justify-content: center; align-items: center; gap: 5px;
    font-size: 8.5px; letter-spacing: .3px; text-transform: uppercase; white-space: nowrap;
  }
  .icon { width: 10px; height: 10px; display: block; flex: none; }

  .back-site {
    position: absolute; top: 11px; left: 70px; right: 14px;
    display: flex; justify-content: flex-end; align-items: center; gap: 5px;
    font-size: 8px; text-transform: uppercase; white-space: nowrap;
  }
  .rep {
    position: absolute; left: 62px; right: 0; top: 34px; text-align: center; white-space: nowrap;
  }
  .rep__name { font-size: 13px; text-transform: uppercase; letter-spacing: 1px; line-height: 18px; }
  .rep__title { font-family: "Cormorant SC", serif; font-size: 13px; line-height: 18px; }
  .rep__email { font-size: 9.5px; line-height: 18px; color: var(--ink-soft); }
  .rep__licence { font-family: "Cormorant SC", serif; font-size: 12px; line-height: 18px; }
  .card--back-teal .rep__name, .card--back-teal .phone { color: var(--teal); }
  .card--back-rose .rep__name, .card--back-rose .phone { color: var(--rose); }
  .phone {
    position: absolute; left: 62px; right: 0; top: 124px;
    display: flex; justify-content: center; align-items: center; gap: 6px;
    font-family: "Cormorant SC", serif; font-size: 12px; white-space: nowrap;
  }
  .rule { position: absolute; left: 110px; right: 30px; top: 144px; height: 1.5px; }
  .card--back-teal .rule { background: var(--teal); }
  .card--back-rose .rule { background: var(--rose); }
</style>
</head>
<body>
  <div class="swatch swatch--teal"></div>
  <div class="swatch swatch--rose"></div>

  <section class="card card--front-teal">
    <div class="facets facets--teal facets--right" role="img" aria-label="Faceted teal diamond pattern"></div>
    <p class="wordmark"><span class="wordmark__name">Brisko</span><span class="wordmark__line">Bike Brands</span></p>
    <p class="site">
      <svg class="icon" viewBox="0 0 10 10"><rect width="10" height="10" rx="1" fill="#f4f4f4"/><path d="M2 5 5 2.3 8 5V8H2Z" fill="#222"/></svg>
      www.briskobikebrands-example.ae
    </p>
  </section>

  <section class="card card--back-teal">
    <div class="facets facets--teal facets--left" role="img" aria-label="Faceted teal diamond pattern"></div>
    <p class="back-site">
      <svg class="icon" viewBox="0 0 10 10"><rect width="10" height="10" rx="1" fill="#f4f4f4"/><path d="M2 5 5 2.3 8 5V8H2Z" fill="#222"/></svg>
      www.briskobikebrands-example.ae
    </p>
    <div class="rep">
      <p class="rep__name">Dorian Pelt</p>
      <p class="rep__title">Managing Director</p>
      <p class="rep__email">E dorian@briskobikebrands-example.ae</p>
      <p class="rep__licence">Trade Lic. No. TBA</p>
    </div>
    <p class="phone">
      <svg class="icon" viewBox="0 0 10 10"><rect width="10" height="10" rx="1" fill="#f4f4f4"/><path d="M3 2.5h1.5l.6 1.6-1 .7a4 4 0 0 0 1.6 1.6l.7-1 1.6.6V7.5A5 5 0 0 1 3 2.5Z" fill="#222"/></svg>
      M +971 (0) 56 482 3107
    </p>
    <div class="rule"></div>
  </section>

  <section class="card card--front-rose">
    <div class="facets facets--rose facets--left" role="img" aria-label="Faceted rose diamond pattern"></div>
    <div class="facets facets--rose facets--right" role="img" aria-label="Faceted rose diamond pattern"></div>
    <p class="wordmark"><span class="wordmark__name">Brisko</span><span class="wordmark__line">Bike Brands</span></p>
    <p class="site">
      <svg class="icon" viewBox="0 0 10 10"><rect width="10" height="10" rx="1" fill="#f4f4f4"/><path d="M2 5 5 2.3 8 5V8H2Z" fill="#222"/></svg>
      www.briskobikebrands-example.ae
    </p>
  </section>

  <section class="card card--back-rose">
    <div class="facets facets--rose facets--left" role="img" aria-label="Faceted rose diamond pattern"></div>
    <p class="back-site">
      <svg class="icon" viewBox="0 0 10 10"><rect width="10" height="10" rx="1" fill="#f4f4f4"/><path d="M2 5 5 2.3 8 5V8H2Z" fill="#222"/></svg>
      www.briskobikebrands-example.ae
    </p>
    <div class="rep">
      <p class="rep__name">Minna Pelt</p>
      <p class="rep__title">Account Manager</p>
      <p class="rep__email">E minna@briskobikebrands-example.ae</p>
      <p class="rep__licence">Trade Lic. No. TBA</p>
    </div>
    <p class="phone">
      <svg class="icon" viewBox="0 0 10 10"><rect width="10" height="10" rx="1" fill="#f4f4f4"/><path d="M3 2.5h1.5l.6 1.6-1 .7a4 4 0 0 0 1.6 1.6l.7-1 1.6.6V7.5A5 5 0 0 1 3 2.5Z" fill="#222"/></svg>
      P +971 (0) 56 916 2583
    </p>
    <div class="rule"></div>
  </section>
</body>
</html>
```